Website design for lighting products company

We want a design for our website. The website is for a company that sells lighting products. The structure is similar to the below website. We really like their design as well: www.ambervalelamps.com

Industry/Entity Type

Lighting

Number of Pages Required

5+ page

Colors

Designer to choose colors to be used in the design.

Requirements
Must have
• Simple design

```html
<!DOCTYPE html>
<html lang="en">
<head>
<meta charset="utf-8">
<title>Lumora Lighting</title>
<link href="https://fonts.googleapis.com/css2?family=Mulish:wght@400;600;700;800&display=swap" rel="stylesheet">
<style>
:root{
  --orange:#f8a51b;
  --dark:#2d2b2c;
  --ink:#333132;
  --text:#4a4a4a;
  --white:#ffffff;
  --line:#d9d9d9;
}
*{margin:0;padding:0;box-sizing:border-box}
html,body{width:1200px;height:3582px;overflow:hidden}
body{font-family:"Mulish",sans-serif;background:var(--white);color:var(--text);position:relative}
.abs{position:absolute}
.btn{position:absolute;display:flex;align-items:center;justify-content:center;gap:6px;font-weight:700;font-size:18px;clip-path:polygon(10% 0,100% 0,90% 100%,0 100%)}
.btn--orange{background:var(--orange);color:var(--dark)}
.btn--dark{background:#2a2a2c;color:var(--white)}
.accent{color:var(--orange)}
.section-title{position:absolute;left:0;width:1200px;text-align:center;font-size:38px;font-weight:400;color:var(--ink)}
.section-title .accent{font-weight:700}
.lead{position:absolute;left:135px;width:930px;text-align:justify;text-align-last:center;font-size:16px;line-height:36px;color:var(--text)}

/* header */
.header{left:0;top:0;width:1200px;height:120px;background:var(--white)}
.brand{left:90px;top:14px;display:flex;align-items:center;gap:14px}
.brand__mark{width:76px;height:76px;border-radius:50%;background:var(--orange)}
.brand__name{color:var(--orange);font-weight:800;font-size:26px;line-height:32px}
.contact-mini{top:16px;display:flex;align-items:center;gap:10px;font-size:16px;color:var(--ink)}
.contact-mini small{display:block;font-size:16px;color:var(--orange)}
.socials{left:975px;top:26px;display:flex;gap:10px}
.socials span{width:25px;height:25px;background:var(--orange)}
.nav{left:500px;top:88px;display:flex;gap:33px;font-size:16px;color:var(--ink)}
.nav .active{color:var(--orange)}

/* hero */
.hero{left:0;top:120px;width:1200px;height:581px;background:radial-gradient(circle at 250px 300px,#c98a2a 0,#5c4a2a 80px,#1d4a52 230px,#0e2a33 520px,#0a1a22 100%)}
.hero__title{left:540px;top:270px;font-size:62px;font-weight:800;color:var(--orange);letter-spacing:1px}
.hero__text{left:544px;top:346px;width:567px;font-size:18px;line-height:40px;color:var(--white);text-align:justify}

/* about */
.about__panel{left:0;top:1205px;width:837px;height:440px;background:var(--dark)}
.about__photo{left:594px;top:1141px;width:606px;height:441px;background:radial-gradient(circle at 460px 160px,#e8b25a 0,#7a5a36 90px,#3a3230 230px,#1e1b1a 100%)}
.about__title{left:89px;top:1295px;font-size:38px;color:var(--white)}
.about__title .accent{font-weight:700}
.about__text{left:89px;top:1354px;width:477px;font-size:16px;line-height:31.5px;color:var(--white);text-align:justify}

/* products */
.product{top:1899px;width:291px;height:436px;display:flex;align-items:flex-end;justify-content:center;padding-bottom:30px;color:var(--white);font-weight:700;font-size:23px}

/* cases */
.slide{top:2520px;height:394px}
.arrow{width:52px;height:52px;border-radius:50%;background:var(--orange);display:flex;align-items:center;justify-content:center}
.case-card{left:242px;top:2750px;width:406px;height:194px;background:var(--dark);padding:26px 28px}
.case-card h3{font-size:23px;color:var(--orange);font-weight:700}
.case-card p{margin-top:12px;font-size:12.5px;line-height:27px;color:var(--white);text-align:justify}
.dots{left:923px;top:2932px;display:flex;gap:5px}
.dots span{width:13px;height:13px;border-radius:50%;border:1.5px solid var(--orange)}
.dots .on{background:var(--orange)}

/* contact */
.map{left:0;top:3089px;width:598px;height:386px;background:linear-gradient(135deg,#e8efe0,#d5e6c8 50%,#e6ecdf)}
.map__pin{left:272px;top:3254px;display:flex;gap:10px;font-size:14px;color:var(--ink);line-height:22px}
.form{left:599px;top:3089px;width:601px;height:386px;background:var(--dark)}
.field{position:absolute;background:var(--white);border-radius:3px;font-size:14px;color:#777;padding:12px 9px}
.form__info{display:flex;align-items:center;gap:8px;color:var(--white)}

/* footer */
.footer{left:0;top:3475px;width:1200px;height:107px;background:var(--white)}
.copy{left:440px;top:3530px;font-size:16px;color:var(--ink)}
.social-ring{left:969px;top:3522px;display:flex;gap:6px}
.social-ring span{width:31px;height:31px;border-radius:50%;border:2px solid var(--dark)}
</style>
</head>
<body>

<header class="abs header">
  <svg class="abs" style="left:0;top:0" width="430" height="120" viewBox="0 0 430 120">
    <polygon points="0,0 350,0 430,120 0,120" fill="#2d2b2c"/>
    <line x1="290" y1="0" x2="370" y2="120" stroke="#fff" stroke-width="2"/>
    <line x1="305" y1="0" x2="385" y2="120" stroke="#fff" stroke-width="2"/>
    <line x1="320" y1="0" x2="400" y2="120" stroke="#fff" stroke-width="2"/>
  </svg>
  <div class="abs brand">
    <span class="brand__mark"></span>
    <span class="brand__name">LUMORA<br>LIGHTING</span>
  </div>
  <div class="abs contact-mini" style="left:578px">
    <svg width="42" height="42" viewBox="0 0 42 42"><circle cx="21" cy="21" r="19" fill="none" stroke="#f8a51b" stroke-width="2.5"/><path d="M14 12c2-1 3 0 4 3l-2 2c1 3 4 6 7 7l2-2c3 1 4 2 3 4-1 3-4 3-7 2-5-2-8-6-9-10-1-3 0-5 2-6z" fill="#f8a51b"/></svg>
    <div>Call Us:<small>+1 555.014.2270</small></div>
  </div>
  <div class="abs contact-mini" style="left:775px">
    <svg width="44" height="44" viewBox="0 0 44 44"><circle cx="17" cy="17" r="13" fill="none" stroke="#f8a51b" stroke-width="2.5"/><line x1="26" y1="26" x2="41" y2="41" stroke="#f8a51b" stroke-width="4" stroke-linecap="round"/></svg>
    <div>Search:<small>Enter search here</small></div>
  </div>
  <div class="abs socials"><span></span><span></span><span></span><span></span></div>
  <svg class="abs" style="left:517px;top:71px" width="18" height="18" viewBox="0 0 18 18"><circle cx="9" cy="8" r="6.5" fill="none" stroke="#f8a51b" stroke-width="1.5"/><path d="M9 14.5v3" stroke="#f8a51b" stroke-width="1.5"/></svg>
  <nav class="abs nav">
    <span class="active">HOME</span><span>ABOUT US</span><span>OUR PRODUCTS</span><span>CASE STUDIES</span><span>CONTACT US</span>
  </nav>
</header>

<section class="abs hero" role="img" aria-label="Glowing light bulb hanging against a dark teal background with soft bokeh lights"></section>
<h1 class="abs hero__title">LUMORA LIGHTING</h1>
<p class="abs hero__text">Lorem ipsum dolor sit amet, consectetur adipiscing elit, sed do eiusmod tempor incididunt ut labore et dolore magna aliqua. Quis ipsum suspendisse ultrices gravida.</p>
<a class="btn btn--orange" style="left:543px;top:479px;width:220px;height:53px">Read More ➔</a>
<a class="btn btn--dark" style="left:771px;top:479px;width:215px;height:53px">Get In Touch ➔</a>

<h2 class="section-title" style="top:783px">Welcome to <span class="accent">Lumora Lighting</span></h2>
<p class="lead" style="top:845px">Sed ut perspiciatis unde omnis iste natus error sit voluptatem accusantium doloremque laudantium, totam rem aperiam, eaque ipsa quae ab illo inventore veritatis et quasi architecto beatae vitae dicta sunt explicabo. Nemo enim ipsam voluptatem quia voluptas sit aspernatur aut odit aut fugit, sed voluptatem sequi nesciunt.</p>
<a class="btn btn--orange" style="left:491px;top:973px;width:218px;height:53px">Read More ➔</a>

<div class="abs about__panel"></div>
<div class="abs about__photo" role="img" aria-label="Filament bulbs inside black geometric cube pendant frames"></div>
<h2 class="abs about__title">About <span class="accent">Lumora Lighting</span></h2>
<p class="abs about__text">Sed ut perspiciatis unde omnis iste natus error sit voluptatem accusantium doloremque laudantium, totam rem aperiam, eaque ipsa quae ab illo inventore veritatis et quasi architecto beatae vitae dicta sunt explicabo.</p>
<a class="btn btn--orange" style="left:89px;top:1492px;width:217px;height:53px">Read More ➔</a>

<h2 class="section-title" style="top:1752px">Our <span class="accent">Products</span></h2>
<p class="lead" style="top:1807px">Sed ut perspiciatis unde omnis iste natus error sit voluptatem accusantium doloremque laudantium, totam rem aperiam, eaque ipsa quae ab illo inventore veritatis et quasi architecto beatae vitae dicta sunt explicabo.</p>
<div class="abs product" style="left:0;background:radial-gradient(circle at 135px 230px,#b8742a 0,#4a2e1c 90px,#141212 230px)" role="img" aria-label="Hanging filament bulb indoor light">Indoor Lights</div>
<div class="abs product" style="left:303px;background:radial-gradient(circle at 180px 170px,#f0c060 0,#7a5520 90px,#262420 240px)" role="img" aria-label="Wall-mounted outdoor lantern lit at night">Outdoor Lights</div>
<div class="abs product" style="left:606px;background:radial-gradient(circle at 150px 190px,#f59a18 0,#c0281a 90px,#3a0c0c 240px)" role="img" aria-label="Red caged emergency light">Emergency Lights</div>
<div class="abs product" style="left:909px;background:radial-gradient(circle at 100px 180px,#d8b070 0,#4a4a30 110px,#1e2218 250px)" role="img" aria-label="Garden lights among plants in the evening">Lighting Controls</div>

<h2 class="section-title" style="top:2443px">Case <span class="accent">Studies</span></h2>
<div class="abs slide" style="left:0;width:153px;background:linear-gradient(135deg,#c9a690,#8c6a58)" role="img" aria-label="Person holding string lights"></div>
<div class="abs slide" style="left:206px;width:788px;background:radial-gradient(circle at 610px 300px,#6ad0f0 0,#1a5f96 130px,#0d2a52 330px,#081528 100%)" role="img" aria-label="Light bulb filled with a starry night sky"></div>
<div class="abs slide" style="left:1045px;width:155px;background:linear-gradient(160deg,#5a5550,#2e2a28)" role="img" aria-label="Street with hanging lights at dusk"></div>
<div class="abs arrow" style="left:180px;top:2685px"><svg width="22" height="14" viewBox="0 0 22 14"><path d="M21 7H3M8 1L2 7l6 6" stroke="#2d2b2c" stroke-width="3" fill="none"/></svg></div>
<div class="abs arrow" style="left:967px;top:2685px"><svg width="22" height="14" viewBox="0 0 22 14"><path d="M1 7h18M14 1l6 6-6 6" stroke="#2d2b2c" stroke-width="3" fill="none"/></svg></div>
<div class="abs case-card">
  <h3>Sed ut perspiciatis unde omnis</h3>
  <p>Sed ut perspiciatis unde omnis iste natus error sit voluptatem accusantium doloremque laudantium, totam rem aperiam, eaque ipsa quae sunt explicabo.</p>
</div>
<a class="btn btn--orange" style="left:271px;top:2919px;width:216px;height:53px">Read More ➔</a>
<div class="abs dots"><span></span><span></span><span class="on"></span><span></span></div>

<div class="abs map" role="img" aria-label="Road map of the region around the office location"></div>
<div class="abs map__pin">
  <svg width="18" height="24" viewBox="0 0 18 24"><path d="M9 1C4 1 1 5 1 9c0 6 8 14 8 14s8-8 8-14c0-4-3-8-8-8z" fill="#e02020"/><circle cx="9" cy="9" r="3" fill="#fff"/></svg>
  <span>2870 Cedar Ridge Lane, Millbrook<br>Ohio - 40012</span>
</div>
<div class="abs form">
  <div class="field" style="left:31px;top:39px;width:233px;height:40px">First Name</div>
  <div class="field" style="left:278px;top:39px;width:234px;height:40px">Last Name</div>
  <div class="field" style="left:31px;top:94px;width:233px;height:41px">Email</div>
  <div class="field" style="left:278px;top:94px;width:234px;height:41px">Phone Number</div>
  <div class="field" style="left:31px;top:151px;width:481px;height:104px">Message</div>
  <a class="btn btn--orange" style="left:34px;top:269px;width:159px;height:42px">Submit</a>
  <div class="abs" style="left:31px;top:328px;width:481px;height:1px;background:#555"></div>
  <div class="abs" style="left:249px;top:338px;width:1px;height:42px;background:#555"></div>
  <div class="abs form__info" style="left:33px;top:345px;font-size:22px;font-weight:700">
    <svg width="18" height="18" viewBox="0 0 18 18"><path d="M3 1c2-1 3 0 4 3L5 6c1 3 4 6 7 7l2-2c3 1 4 2 3 4-1 3-4 3-7 2C5 15 2 11 1 7 0 4 1 2 3 1z" fill="#fff"/></svg>
    555 010 4477
  </div>
  <div class="abs form__info" style="left:285px;top:338px;font-size:13px;line-height:20px">
    <svg width="16" height="22" viewBox="0 0 18 24"><path d="M9 1C4 1 1 5 1 9c0 6 8 14 8 14s8-8 8-14c0-4-3-8-8-8z" fill="#fff"/><circle cx="9" cy="9" r="3" fill="#2d2b2c"/></svg>
    <span>47 Harbor Avenue, Fairview, Oregon<br>97001</span>
  </div>
</div>

<footer class="abs footer"></footer>
<div class="abs brand" style="top:3485px">
  <span class="brand__mark"></span>
  <span class="brand__name">LUMORA<br>LIGHTING</span>
</div>
<p class="abs copy">Lumora Lighting © 2019. All Rights Reserved.</p>
<div class="abs social-ring"><span></span><span></span><span></span><span></span></div>

</body>
</html>
```